business card for LWR pty ltd

We require a business card that stands out . I have included our company flyer and would like the services listed to be put on the card so when we Give out the cards to customers they have an idea of services we provide. need the winning design to be in editable photo shop format, editable iMac pages format or editable windows publisher format, so that I can enter in names, email addresses, phone numbers etc myself. I have included a pdf documents of info / items needed on the card to use as reference please.
Updates

need more submissions

Need extra days to review

Sick

Target Market(s)

new customers

Contact Information for Business Card

details are on attached business card requirements file

Requirements
Must have
• I have attached a list of must haves

```html
<!DOCTYPE html>
<html lang="en">
<head>
<meta charset="utf-8">
<title>LWR Pty Ltd – Business Card</title>
<link href="https://fonts.googleapis.com/css2?family=Poppins:wght@400;500;600&display=swap" rel="stylesheet">
<style>
  :root {
    --backdrop: #1c1c1e;
    --card-dark: #2a2420;
    --card-black: #0c0c0d;
    --gold: #a68443;
    --gold-band: #957338;
    --text-light: #f3efe8;
    --logo-silver: #c9ccd1;
    --dirt-1: #b46a3a;
    --dirt-2: #d89a66;
    --sky-dark: #1a1715;
  }
  * { box-sizing: border-box; margin: 0; padding: 0; }
  html, body {
    width: 1200px; height: 900px; overflow: hidden;
    background: var(--backdrop);
    font-family: "Poppins", sans-serif;
  }
  .stage {
    width: 1200px; height: 900px;
    display: flex; flex-direction: column;
    align-items: center; justify-content: center; gap: 50px;
  }
  .card {
    width: 580px; height: 350px;
    position: relative; overflow: hidden;
    box-shadow: 0 12px 30px rgba(0,0,0,.5);
  }

  /* Front */
  .card-front { background: var(--card-dark); }
  .front-photo {
    position: absolute; left: 0; top: 0; width: 330px; height: 350px;
    background:
      linear-gradient(90deg, rgba(42,36,32,0) 55%, var(--card-dark) 100%),
      radial-gradient(ellipse at 35% 45%, #b9bec4 0%, #6e7075 35%, #3a3532 65%, var(--card-dark) 100%);
  }
  .front-details {
    position: absolute; right: 34px; top: 34px;
    text-align: right; color: var(--text-light);
  }
  .person-name {
    color: var(--gold); font-weight: 600; font-size: 22px;
    letter-spacing: 1.5px; text-transform: uppercase; line-height: 1.1;
  }
  .person-role { font-size: 14px; margin-top: 4px; }
  .divider {
    width: 46px; height: 3px; background: var(--gold);
    margin: 22px 0 18px auto;
  }
  .company-name { color: var(--gold); font-size: 15px; font-weight: 500; }
  .address-line { font-size: 13px; line-height: 1.5; }
  .contact-list { list-style: none; margin-top: 10px; }
  .contact-item {
    display: flex; justify-content: flex-end; align-items: center; gap: 8px;
    font-size: 13px; line-height: 1.6;
  }
  .contact-item svg { width: 12px; height: 12px; fill: var(--gold); flex: none; }

  /* Back */
  .card-back { background: var(--card-black); }
  .back-texture {
    position: absolute; left: 0; top: 0; width: 100%; height: 120px;
    background: linear-gradient(180deg, #18191b 0%, var(--card-black) 100%);
  }
  .brand-name {
    position: absolute; right: 40px; top: 26px;
    font-size: 64px; font-weight: 600; letter-spacing: 4px; line-height: 1;
    color: var(--logo-silver);
  }
  .back-photo {
    position: absolute; left: 0; top: 60px; width: 100%; height: 180px;
    background:
      linear-gradient(180deg, rgba(12,12,13,.9) 0%, rgba(12,12,13,0) 30%),
      linear-gradient(180deg, var(--sky-dark) 0%, #3a302a 35%, var(--dirt-1) 60%, var(--dirt-2) 100%);
  }
  .services-band {
    position: absolute; left: 0; bottom: 0; width: 100%; height: 110px;
    background: var(--gold-band);
    display: flex; flex-direction: column; justify-content: center; align-items: flex-end;
    padding: 0 22px; color: var(--text-light);
    font-size: 11.2px; line-height: 1.55; text-align: right;
  }
</style>
</head>
<body>
<main class="stage">

  <section class="card card-front" aria-label="Business card front">
    <div class="front-photo" role="img" aria-label="Chrome-fronted road train prime mover"></div>
    <div class="front-details">
      <h1 class="person-name">Daniel Harper</h1>
      <p class="person-role">Director</p>
      <div class="divider"></div>
      <p class="company-name">LWR Pty Ltd</p>
      <p class="address-line">Depot: Lot 444</p>
      <p class="address-line">example address Australia</p>
      <ul class="contact-list">
        <li class="contact-item">000 444 000
          <svg viewBox="0 0 24 24" aria-hidden="true"><path d="M6.6 10.8a15.1 15.1 0 0 0 6.6 6.6l2.2-2.2a1 1 0 0 1 1-.25 11.4 11.4 0 0 0 3.6.57 1 1 0 0 1 1 1V20a1 1 0 0 1-1 1A17 17 0 0 1 3 4a1 1 0 0 1 1-1h3.5a1 1 0 0 1 1 1c0 1.25.2 2.45.57 3.57a1 1 0 0 1-.25 1z"/></svg>
        </li>
        <li class="contact-item">email@lwrhaulage.com.au
          <svg viewBox="0 0 24 24" aria-hidden="true"><path d="M2 5h20v14H2z M2 5l10 8 10-8" stroke="#2a2420" stroke-width="1.6"/></svg>
        </li>
        <li class="contact-item">www.websiteaddress.com
          <svg viewBox="0 0 24 24" aria-hidden="true"><circle cx="12" cy="12" r="10"/><path d="M2 12h20M12 2c3 3 3 17 0 20M12 2c-3 3-3 17 0 20" stroke="#2a2420" stroke-width="1.4" fill="none"/></svg>
        </li>
      </ul>
    </div>
  </section>

  <section class="card card-back" aria-label="Business card back">
    <div class="back-photo" role="img" aria-label="Road train with side tippers on red outback dirt"></div>
    <div class="back-texture"></div>
    <div class="brand-name">LWR</div>
    <div class="services-band">
      <p>Over Size Loads / Hot Shot Loads | Heavy Vehicle Recovery Services</p>
      <p>Potable Water Deliveries | Road, Building / Mamaintenance | Earthworks</p>
      <p>Sand &amp; Metal Supply &amp; Cartage | Road Train Tippers | Road Train Trankers</p>
      <p>Road Train Flat Tops | Drop Deck Trailers | Mine Site accredited equipment &amp; Operators</p>
    </div>
  </section>

</main>
</body>
</html>
```